a Label for a candle jar and its gift box

I would like a label that is modern minimalist for candles jars. These jars are colored as white, amber and black. I am thinking maybe foiling gold/silver background with logo only and maybe company name in different color that suits the foiling background color/s. I would like a high quality luxurious design that shows the preciousness of this candle. I am open to any ideas you might have for the design but so far I have used a logo only on the jar which I really like BUT I still feel that it is not enough branding for people when you only show them the logo so I am considering adding the business name. Again, I am open to both ideas (with logo only or logo with business name (Velvet Lantern).

IMPORTANT: YOU MAY IGNORE MY DESIGN COMPLETELY AND DO YOUR OWN ONE AS LONG AS YOU KERP THE LOGO DESIGN. YOU MAY ALSO ADJUST THE LOGO A BIT TO SUIT YOUR DESIGN. - sorry im using capital letters to show importance but im not yelling :)
Updates

UPDATE: To clarify, I have uploaded a video called Corvale in the box to show what the current product look like. It is a corvale jar with a logo only and the jar box has a window that shows the jar with the logo on it and the back of that jar box has a bigger version of the label that has more details (i.e. Fragrance name and website link). So to make it clear, I would like to have two versions of the lables: 1. on the jar with minimal info (logo only or logo with the business name) 2. Bigger version of the label with more info to put on the back of the jar box - as described above. The dimensions of the jars are as per this link https://www.plintova.com.au/corvale-medium-base-and-flat-lid-amber-packed-with-lid-on/ The dimensions of the jar box as per this link https://www.plintova.com.au/corvale-medium-flat-lid-candle-box-with-window-beige/ Looking forward to some artistic productions :)

Update #2: Tues 25 Dec 18 1. I have uploaded the photo which has the logo with the name 'Velvet Lantern' below it just for a reference. However, I would like the designer to modify the current font and NOT to use it as the word 'of in the phrase 'Velvet Lantern' does not come out clear enough after printing. 2. I would like the designer NOT to create a design that will require a clear sticker/label for printing. 3. I have attached the photos of my current designs on the jars or the jar box just as a reference but please do NOT just use the same fonts and only change background. I am hoping to see something different and more professional than my own design :) Thank you very much!

Font styles to use
Decorative
Script

Requirements
Must have
• I would like them to fit on the three colors of the jars below - white, amber and black. Below is a link to how the jar looks like https://www.plintova.com.au/candle-making-supplies/candle-jars/corvale-candle-jars/?glassware_colour=415,443,417&glassware_size=268
Nice to have
• I would like to have a modern design which is suitable for both feminine and musculine.
Should not have
• shouldnt have so much writing on it!

```html
<!DOCTYPE html>
<html lang="en">
<head>
<meta charset="utf-8">
<title>Velvet Lantern — Turkish Rose Labels</title>
<link rel="stylesheet" href="https://fonts.googleapis.com/css2?family=Questrial&display=swap">
<style>
  :root {
    --canvas: #ffffff;
    --card-border: #c8c8c8;
    --ink-black: #000000;
    --gold-dark: #b8902e;
    --gold-light: #e6e66a;
    --gold-text: #c9a24a;
    --brand-gold: #a87a22;
    --bronze-dark: #3a1606;
    --bronze-mid: #8a3a0c;
    --frost: #f2f8fb;
    --silver-dark: #a7aaa8;
    --silver-light: #f1f0ec;
    --silver-text: #a9a9a9;
    --white: #ffffff;
  }
  * { box-sizing: border-box; margin: 0; padding: 0; }
  html, body { width: 1200px; height: 1000px; overflow: hidden; background: var(--canvas); }
  body { position: relative; font-family: "Questrial", "Century Gothic", sans-serif; }

  .label-card {
    position: absolute; top: 84px; width: 230px; height: 312px;
  }
  .label-card--white { left: 230px; background: var(--white); border: 1px solid var(--card-border); }
  .label-card--black { left: 484px; background: var(--ink-black); }
  .label-card--bronze {
    left: 739px;
    background: linear-gradient(90deg, var(--bronze-dark) 0%, var(--bronze-mid) 55%, #a14a10 72%, var(--bronze-dark) 100%);
  }
  .label-card svg { position: absolute; left: 0; top: 0; }

  .brand-mark {
    position: absolute; border-radius: 50%;
  }
  .label-card .brand-mark { left: 91px; top: 108px; width: 48px; height: 48px; }
  .label-card--white .brand-mark { background: var(--gold-text); }
  .label-card--black .brand-mark { background: var(--white); }
  .label-card--bronze .brand-mark { background: var(--brand-gold); }

  .brand-name {
    position: absolute; left: 0; width: 100%; text-align: center;
    font-size: 13px; letter-spacing: 1.4px; text-transform: uppercase; white-space: nowrap;
  }
  .label-card .brand-name { top: 201px; }

  .fragrance-name {
    position: absolute; left: 0; width: 100%; text-align: center;
    font-size: 24px; line-height: 1;
  }
  .label-card .fragrance-name { top: 240px; }

  .label-card--white .brand-name { color: var(--gold-text); }
  .label-card--white .fragrance-name { color: var(--ink-black); }
  .label-card--black .brand-name { color: var(--white); }
  .label-card--black .fragrance-name { color: var(--gold-text); }
  .label-card--bronze .brand-name { color: var(--brand-gold); }
  .label-card--bronze .fragrance-name { color: var(--white); }

  .jar-label {
    position: absolute; left: 492px; top: 556px; width: 210px; height: 250px;
  }
  .jar-label svg { position: absolute; left: 0; top: 0; }
  .jar-label .brand-mark { left: 72px; top: 86px; width: 66px; height: 66px; background: var(--brand-gold); }
  .jar-label .brand-name { top: 202px; font-size: 16px; letter-spacing: 1.6px; color: var(--brand-gold); }
  .jar-fragrance {
    position: absolute; left: 446px; top: 806px; width: 300px; text-align: center;
    font-size: 34px; color: var(--silver-text); transform: rotate(-2deg);
  }
</style>
</head>
<body>

  <section class="label-card label-card--white" aria-label="Label on white">
    <svg width="230" height="312" viewBox="0 0 230 312" aria-hidden="true">
      <path d="M36 103 Q110 62 194 58 L194 230 L36 230 Z" fill="var(--ink-black)"/>
    </svg>
    <span class="brand-mark" aria-hidden="true"></span>
    <p class="brand-name">Velvet Lantern</p>
    <p class="fragrance-name">Turkish Rose</p>
  </section>

  <section class="label-card label-card--black" aria-label="Label on black">
    <svg width="230" height="312" viewBox="0 0 230 312" aria-hidden="true">
      <defs>
        <linearGradient id="gold-foil" x1="0" y1="0" x2="1" y2="1">
          <stop offset="0" stop-color="var(--gold-dark)"/>
          <stop offset="0.6" stop-color="var(--gold-light)"/>
          <stop offset="1" stop-color="var(--gold-dark)"/>
        </linearGradient>
      </defs>
      <path d="M36 103 Q110 62 194 58 L194 230 L36 230 Z" fill="url(#gold-foil)"/>
    </svg>
    <span class="brand-mark" aria-hidden="true"></span>
    <p class="brand-name">Velvet Lantern</p>
    <p class="fragrance-name">Turkish Rose</p>
  </section>

  <section class="label-card label-card--bronze" aria-label="Label on amber">
    <svg width="230" height="312" viewBox="0 0 230 312" aria-hidden="true">
      <path d="M36 103 Q110 62 194 58 L194 230 L36 230 Z" fill="var(--frost)"/>
    </svg>
    <span class="brand-mark" aria-hidden="true"></span>
    <p class="brand-name">Velvet Lantern</p>
    <p class="fragrance-name">Turkish Rose</p>
  </section>

  <section class="jar-label" aria-label="Silver foil jar label">
    <svg width="210" height="250" viewBox="0 0 210 250" aria-hidden="true">
      <defs>
        <linearGradient id="silver-foil" x1="0" y1="0" x2="1" y2="0">
          <stop offset="0" stop-color="var(--silver-dark)"/>
          <stop offset="0.35" stop-color="var(--silver-light)"/>
          <stop offset="0.55" stop-color="var(--silver-light)"/>
          <stop offset="1" stop-color="var(--silver-dark)"/>
        </linearGradient>
      </defs>
      <path d="M0 64 Q100 18 210 4 L210 232 Q105 236 0 246 Z" fill="url(#silver-foil)"/>
    </svg>
    <span class="brand-mark" aria-hidden="true"></span>
    <p class="brand-name">Velvet Lantern</p>
  </section>
  <p class="jar-fragrance">Turkish Rose</p>

</body>
</html>
```